Whitening Flyer

I need an informational flyer for my dental practice. The flyer will describe the whitening services that are available at my practice and show price of each whitening service. We currently gave a 3 fold brochure, but I prefer something with a more professional look, and personalized with our branding and practice colors. I have attached the current flyer for you to use similar text. I will also attach a flyer that I have used in the past that could demonstrate my branding or feel free to view my website: www.grkvemu.com

```html
<!DOCTYPE html>
<html lang="en">
<head>
<meta charset="utf-8">
<title>Whitening Flyer – Brightwell Dental</title>
<link rel="stylesheet" href="https://fonts.googleapis.com/css2?family=Montserrat:wght@400;500;600;700;800&display=swap">
<style>
:root{
  --red:#d0113f;
  --red-dark:#b30d35;
  --yellow:#f7c948;
  --ink:#1d1d1f;
  --text:#333;
  --page:#ededed;
  --paper:#ffffff;
  --silver-a:#f4f4f4;
  --silver-b:#b9b9b9;
  --gold-a:#f6e39a;
  --gold-b:#c9a23c;
}
*{box-sizing:border-box;margin:0;padding:0}
html,body{width:783px;height:1200px;overflow:hidden}
body{background:var(--page);font-family:"Montserrat",sans-serif;color:var(--text)}
.flyer{position:absolute;left:0;top:45px;width:783px;height:1110px;background:var(--paper);overflow:hidden;box-shadow:0 2px 10px rgba(0,0,0,.12)}
.abs{position:absolute}

.brand{left:34px;top:58px;font-size:28px;font-weight:700;color:var(--red);letter-spacing:.3px}
.brand-mark{display:inline-block;width:12px;height:12px;border-radius:50%;background:var(--red);margin-right:8px;vertical-align:middle}

.hero-band{left:0;top:0;width:783px;height:400px}
.title{left:30px;top:158px;font-weight:800;font-size:45px;line-height:46px;color:#fff;letter-spacing:.5px}
.title .accent{color:var(--yellow)}
.title-rule{left:30px;top:310px;width:46px;height:4px;background:var(--yellow)}
.doctor{left:28px;top:330px;font-size:22px;font-weight:700;color:#fff}

.people-photo{left:376px;top:0;width:407px;height:422px}

.section-head{font-size:18px;font-weight:700;color:var(--ink);text-transform:uppercase}
.section-head .hl{color:var(--red)}
.why-head{left:31px;top:396px}
.head-rule{width:24px;height:2px;background:var(--red)}
.why-rule{left:31px;top:418px}
.body-copy{font-size:10.2px;line-height:13px;color:var(--text)}
.why-copy{left:30px;top:436px;width:710px}

.package-head{left:0;top:489px;width:783px;text-align:center;font-size:22px;letter-spacing:.3px}

.package{width:136px;top:538px}
.pill{position:relative;height:48px;border:2px solid #333;border-radius:24px;background:#fff;padding:3px}
.pill::after{content:"";position:absolute;right:28px;top:-5px;width:6px;height:6px;border:1.5px solid #333;border-radius:50%;background:#fff}
.pill-inner{height:38px;border-radius:19px;display:flex;align-items:center;justify-content:space-between;padding:0 6px 0 0}
.pill-name{flex:1;text-align:center;font-weight:700;font-size:14px;color:var(--ink);text-transform:uppercase}
.pill-price{font-weight:700;font-size:13px;color:var(--ink);background:#fff;border-radius:16px;padding:7px 5px 7px 8px}
.pill-price sup{font-size:8px}
.basic .pill-inner{background:var(--red)}
.basic .pill-name{color:#fff}
.silver .pill-inner{background:linear-gradient(180deg,var(--silver-a),var(--silver-b) 55%,#e6e6e6)}
.gold .pill-inner{background:linear-gradient(180deg,var(--gold-a),var(--gold-b) 55%,#ead27a)}
.diamond .pill-inner,.platinum .pill-inner{background:#fff}
.pkg-body{position:relative;height:190px;margin:0 6px 0 6px;border:1.5px solid #333;border-top:none;border-radius:0 0 12px 12px;padding:12px 10px 0;font-size:10.2px;line-height:12.7px;text-align:center;color:var(--text)}
.pkg-body::after{content:"";position:absolute;left:-4px;bottom:6px;width:6px;height:6px;border-radius:50%;background:var(--red)}

.quote{left:172px;top:800px;display:flex;align-items:flex-end;gap:12px;font-size:12px;font-weight:700;color:var(--ink);text-transform:uppercase}
.quote-mark{font-size:56px;line-height:30px;height:28px;color:var(--red);font-weight:800;font-family:Georgia,serif}

.start-head{left:31px;top:841px}
.start-copy{left:31px;top:879px;width:690px}

.factors{left:31px;top:922px;width:720px;display:grid;grid-template-columns:360px 340px;column-gap:3px;row-gap:9px}
.factor{display:flex;gap:10px;font-size:10.2px;line-height:12.7px}
.factor b{color:var(--ink)}
.tick{flex:none;width:14px;height:14px;margin-top:1px}

.footer{left:0;top:1020px;width:783px;height:90px}
.phone{left:32px;top:1033px;font-size:24px;font-weight:700;color:#fff;display:flex;align-items:center;gap:6px}
.address{left:38px;top:1068px;font-size:13px;font-weight:600;color:#fff;display:flex;align-items:center;gap:10px}
.contacts{left:384px;top:1051px;display:flex;align-items:center;gap:16px;font-size:13.5px;font-weight:600;color:var(--ink)}
.contacts span{display:flex;align-items:center;gap:5px}
.social{display:inline-block;width:14px;height:14px;border-radius:2px;background:var(--red)}
.social.blue{background:#3b5a98}
</style>
</head>
<body>
<div class="flyer">

  <svg class="abs hero-band" viewBox="0 0 783 400" aria-hidden="true">
    <path d="M0 137 H373 C360 200 385 320 443 372 H0 Z" fill="var(--red)"/>
    <path d="M0 375 H446 L455 384 H0 Z" fill="var(--yellow)"/>
  </svg>

  <div class="abs brand"><span class="brand-mark"></span>Brightwell Dental</div>

  <svg class="abs people-photo" viewBox="0 0 407 422" role="img" aria-label="Photo collage of smiling patients of all ages, framed in a flower shape">
    <defs>
      <linearGradient id="photoTone" x1="0" y1="0" x2="1" y2="1">
        <stop offset="0" stop-color="#c9a58c"/>
        <stop offset=".45" stop-color="#a85a40"/>
        <stop offset="1" stop-color="#7a4a3c"/>
      </linearGradient>
    </defs>
    <g fill="none" stroke="var(--red)" stroke-width="4">
      <circle cx="110" cy="90" r="62"/><circle cx="210" cy="60" r="62"/><circle cx="325" cy="95" r="62"/>
      <circle cx="70" cy="190" r="60"/><circle cx="355" cy="195" r="58"/><circle cx="95" cy="300" r="62"/>
      <circle cx="320" cy="300" r="60"/><circle cx="205" cy="350" r="62"/>
    </g>
    <g fill="url(#photoTone)">
      <circle cx="110" cy="90" r="62"/><circle cx="210" cy="60" r="62"/><circle cx="325" cy="95" r="62"/>
      <circle cx="70" cy="190" r="60"/><circle cx="355" cy="195" r="58"/><circle cx="95" cy="300" r="62"/>
      <circle cx="320" cy="300" r="60"/><circle cx="205" cy="350" r="62"/><circle cx="210" cy="200" r="120"/>
    </g>
  </svg>

  <h1 class="abs title">WHICH<br><span class="accent">WHITENING</span><br>IS RIGHT?</h1>
  <div class="abs title-rule"></div>
  <p class="abs doctor">Dr. Harlow DMD</p>

  <h2 class="abs section-head why-head"><span class="hl">Why</span> Us</h2>
  <div class="abs head-rule why-rule"></div>
  <p class="abs body-copy why-copy">Our office staff has been trained extensively to assist you step by step in the whitening process. From pre-op to post op, they are by your side to help with questions or concerns Our office offers multiple options fitting every budget. You can also speak with our office manager about possible payment options. Some restrictions may apply and results vary.</p>

  <h2 class="abs section-head package-head">Our Whitening <span class="hl">Package</span></h2>

  <div class="abs package basic" style="left:31px">
    <div class="pill"><div class="pill-inner"><span class="pill-name">Basic</span><span class="pill-price"><sup>$</sup>10</span></div></div>
    <div class="pkg-body">One Upper and Lower one-time use tray set and care instructions.<br>No appointment needed.</div>
  </div>
  <div class="abs package silver" style="left:180px">
    <div class="pill"><div class="pill-inner"><span class="pill-name">Silver</span><span class="pill-price"><sup>$</sup>80</span></div></div>
    <div class="pkg-body">Ten Upper and Lower one-time use trays and care instructions.<br>No appointment needed.</div>
  </div>
  <div class="abs package gold" style="left:326px">
    <div class="pill"><div class="pill-inner"><span class="pill-name">Gold</span><span class="pill-price"><sup>$</sup>275</span></div></div>
    <div class="pkg-body">Custom made upper and lower whitening trays to be used at home. One 30 min office appointment for impressions. 4 tubes of professional whitening agent. At home care instructions (refills available for purchase of $35)</div>
  </div>
  <div class="abs package diamond" style="left:470px">
    <div class="pill"><div class="pill-inner"><span class="pill-name">Diamond</span><span class="pill-price"><sup>$</sup>375</span></div></div>
    <div class="pkg-body">One 90 min office appointment for chairside Lumina Gel whitening. At home care instructions.</div>
  </div>
  <div class="abs package platinum" style="left:614px">
    <div class="pill"><div class="pill-inner"><span class="pill-name">Platinum</span><span class="pill-price"><sup>$</sup>475</span></div></div>
    <div class="pkg-body">One 2hr office appointment for chairside Lumina Gel whitening. At home care instructions.</div>
  </div>

  <p class="abs quote"><span class="quote-mark">&ldquo;</span>At Brightwell Dental, we care about your smile</p>

  <h2 class="abs section-head start-head"><span class="hl">How do you</span> get started?</h2>
  <p class="abs body-copy start-copy">There are many options and factors to take into account when deciding which whitening option is best for you. Our team is here to help you in the decision process. Some deciding factors include;</p>

  <div class="abs factors">
    <div class="factor">
      <svg class="tick" viewBox="0 0 14 14" aria-hidden="true"><circle cx="7" cy="7" r="7" fill="var(--red)"/><path d="M3.8 7.2 6 9.3 10.3 4.8" fill="none" stroke="#fff" stroke-width="1.8"/></svg>
      <p><b>The Cost:</b> cost can range anywhere from $30 for oer the counter treatment to $600 for some in office treatments</p>
    </div>
    <div class="factor">
      <svg class="tick" viewBox="0 0 14 14" aria-hidden="true"><circle cx="7" cy="7" r="7" fill="var(--red)"/><path d="M3.8 7.2 6 9.3 10.3 4.8" fill="none" stroke="#fff" stroke-width="1.8"/></svg>
      <p><b>The Sensitivity:</b> If you suffer from sensitive gums or teeth some of the stronger treatments may not be tats) best option for you.</p>
    </div>
    <div class="factor">
      <svg class="tick" viewBox="0 0 14 14" aria-hidden="true"><circle cx="7" cy="7" r="7" fill="var(--red)"/><path d="M3.8 7.2 6 9.3 10.3 4.8" fill="none" stroke="#fff" stroke-width="1.8"/></svg>
      <p><b>The Effort:</b> In office treatment can take as little time as 1 1/2 hours whereas over the counter treatment can take up to 3 weeks to see a difference.</p>
    </div>
    <div class="factor">
      <svg class="tick" viewBox="0 0 14 14" aria-hidden="true"><circle cx="7" cy="7" r="7" fill="var(--red)"/><path d="M3.8 7.2 6 9.3 10.3 4.8" fill="none" stroke="#fff" stroke-width="1.8"/></svg>
      <p><b>The RESULTS:</b> There is a significant difference in the active whitening ingredient that is allowed in OTC products vs. In office solutions. Typically; a professional solution will make your teeth brighter, faster</p>
    </div>
  </div>

  <svg class="abs footer" viewBox="0 0 783 90" aria-hidden="true">
    <path d="M0 10 H310 C345 14 360 60 392 90 H0 Z" fill="var(--red)"/>
    <path d="M310 10 C350 10 372 55 404 90 H396 C368 60 350 24 318 12 Z" fill="var(--yellow)"/>
  </svg>
  <p class="abs phone">
    <svg width="18" height="18" viewBox="0 0 24 24" aria-hidden="true"><path d="M6.6 10.8a15 15 0 0 0 6.6 6.6l2.2-2.2a1 1 0 0 1 1-.25 11.4 11.4 0 0 0 3.6.57 1 1 0 0 1 1 1V20a1 1 0 0 1-1 1A17 17 0 0 1 3 4a1 1 0 0 1 1-1h3.5a1 1 0 0 1 1 1c0 1.25.2 2.45.57 3.57a1 1 0 0 1-.25 1z" fill="var(--yellow)"/></svg>
    (504)555-0148
  </p>
  <p class="abs address">
    <svg width="11" height="15" viewBox="0 0 12 16" aria-hidden="true"><path d="M6 0a6 6 0 0 0-6 6c0 4.5 6 10 6 10s6-5.5 6-10a6 6 0 0 0-6-6zm0 8.2A2.2 2.2 0 1 1 6 3.8a2.2 2.2 0 0 1 0 4.4z" fill="var(--yellow)"/></svg>
    1180 Larkin Ave, Riverton, LA, 70400
  </p>
  <div class="abs contacts">
    <span><svg width="12" height="9" viewBox="0 0 12 9" aria-hidden="true"><rect width="12" height="9" fill="var(--red)"/><path d="M0 0 6 5 12 0" fill="none" stroke="#fff" stroke-width="1"/></svg>info@grkvemu.com</span>
    <span><svg width="12" height="12" viewBox="0 0 12 12" aria-hidden="true"><g fill="none" stroke="var(--red)" stroke-width="1.1"><circle cx="6" cy="6" r="5.3"/><ellipse cx="6" cy="6" rx="2.4" ry="5.3"/><path d="M.7 6h10.6M1.6 3.3h8.8M1.6 8.7h8.8"/></g></svg>www.grkvemu.com</span>
    <span><i class="social blue"></i><i class="social"></i></span>
  </div>

</div>
</body>
</html>
```